Stationary for Travel & Tourism Co.
KBR Stationary
Stationary for Travel & Tourism Co. - Travel
Creative Brief
Professional
Tariq Hamdoun Salwi
IT Manager
Office No.627, Noor Plaza Al Hamra Dist. - Prince Fahd Street P.B No.38271 Jeddah 27390 Kingdom of Saudi Arabia
+966 2 6583917 X 482
t.salwi@gokbrtrips.com
www.gokbrtrips.com
The horse object in the logo is advised to be nicely embosed as watermark on the stationary particularly on the letter head.

```html
<!DOCTYPE html>
<html lang="en">
<head>
<meta charset="utf-8">
<title>KBR Travel &amp; Tourism Co — Business Card</title>
<link rel="stylesheet" href="https://fonts.googleapis.com/css2?family=Raleway:wght@500;600;700;800&display=swap">
<style>
  :root {
    --page-bg: #e9e7e4;
    --card-bg: #ffffff;
    --brand-red: #b3121d;
    --brand-red-dark: #7e0a12;
    --ink: #3a3a3a;
    --ink-soft: #6b6b6b;
    --rule-dark: #3d3d3d;
    --band-text: #ffffff;
  }
  * { margin: 0; padding: 0; box-sizing: border-box; }
  html, body {
    width: 1200px; height: 914px; overflow: hidden;
    background: var(--page-bg);
    font-family: "Raleway", "Helvetica Neue", Arial, sans-serif;
  }
  .canvas {
    position: relative; width: 1200px; height: 914px;
    display: flex; align-items: center; justify-content: center;
  }
  .business-card {
    position: relative; width: 1000px; height: 570px;
    background: var(--card-bg);
    box-shadow: 0 10px 30px rgba(0,0,0,0.15);
  }
  .brand {
    position: absolute; left: 0; right: 0; top: 78px;
    display: flex; flex-direction: column; align-items: center;
    transform: translateX(-90px);
  }
  .brand-mark { display: flex; align-items: center; gap: 18px; }
  .brand-square { width: 34px; height: 34px; background: var(--brand-red); }
  .brand-name {
    font-size: 118px; font-weight: 800; letter-spacing: 10px;
    color: var(--brand-red); line-height: 1;
  }
  .brand-tagline {
    margin-top: 10px;
    font-size: 22px; font-weight: 700; letter-spacing: 1.5px;
    color: var(--brand-red-dark); text-transform: uppercase;
  }
  .identity-band {
    position: absolute; left: 0; right: 0; top: 268px; height: 66px;
    background: linear-gradient(180deg, #c8202b 0%, var(--brand-red) 55%, var(--brand-red-dark) 100%);
    display: flex; align-items: center; justify-content: flex-end;
    padding-right: 250px;
  }
  .identity-band .holder {
    color: var(--band-text); font-size: 26px; font-weight: 700;
    font-variant: small-caps; letter-spacing: 2px; white-space: nowrap;
  }
  .identity-band .divider { margin: 0 14px; font-weight: 500; }
  .band-rule {
    position: absolute; left: 0; right: 0; top: 340px; height: 12px;
    background: var(--rule-dark);
  }
  .address {
    position: absolute; left: 42px; right: 30px; top: 380px;
    font-size: 15px; font-weight: 600; color: var(--ink);
    font-variant: small-caps; letter-spacing: 0.6px; white-space: nowrap;
  }
  .address svg { width: 15px; height: 15px; vertical-align: -2px; margin-right: 6px; }
  .contact-row {
    position: absolute; left: 42px; right: 30px; top: 420px;
    display: flex; justify-content: space-between;
    list-style: none;
  }
  .contact-row li {
    display: flex; align-items: center; gap: 8px;
    font-size: 15px; font-weight: 600; color: var(--ink-soft);
    font-variant: small-caps; letter-spacing: 0.5px; white-space: nowrap;
  }
  .contact-row svg { width: 16px; height: 16px; flex: none; }
</style>
</head>
<body>
<main class="canvas">
  <article class="business-card">
    <header class="brand">
      <div class="brand-mark">
        <span class="brand-square" aria-hidden="true"></span>
        <span class="brand-name">KBR</span>
      </div>
      <p class="brand-tagline">KBR Travel &amp; Tourism Co</p>
    </header>

    <div class="identity-band">
      <p class="holder">Tariq Hamdoun Salwi<span class="divider">|</span>IT Manager</p>
    </div>
    <div class="band-rule"></div>

    <p class="address"><svg viewBox="0 0 16 16" aria-hidden="true"><circle cx="8" cy="8" r="7" fill="var(--brand-red)"/><path d="M8 4a2.6 2.6 0 0 0-2.6 2.6C5.4 9 8 12 8 12s2.6-3 2.6-5.4A2.6 2.6 0 0 0 8 4z" fill="#fff"/></svg>Office No.627, Noor Plaza Al Hamra Dist. - Prince Fahd Street P.B No.38271 Jeddah 27390 Kingdom of Saudi Arabia</p>

    <ul class="contact-row">
      <li><svg viewBox="0 0 16 16" aria-hidden="true"><circle cx="8" cy="8" r="7" fill="var(--brand-red)"/><path d="M5.5 4.5l1.5 0 .7 2-1 .8a5 5 0 0 0 2 2l.8-1 2 .7v1.5a1 1 0 0 1-1 1A6.5 6.5 0 0 1 4.5 5.5a1 1 0 0 1 1-1z" fill="#fff"/></svg>+966 2 6583917 X 482</li>
      <li><svg viewBox="0 0 16 16" aria-hidden="true"><circle cx="8" cy="8" r="7" fill="var(--brand-red)"/><rect x="5.5" y="3.8" width="5" height="8.4" rx="1" fill="#fff"/></svg>+966 507214396</li>
      <li><svg viewBox="0 0 16 16" aria-hidden="true"><circle cx="8" cy="8" r="7" fill="var(--brand-red)"/><rect x="4.5" y="6" width="7" height="5" fill="#fff"/><rect x="6" y="4" width="4" height="2.5" fill="#fff"/></svg>+966 2 6583920</li>
      <li><svg viewBox="0 0 16 16" aria-hidden="true"><circle cx="8" cy="8" r="7" fill="var(--brand-red)"/><rect x="4" y="5.5" width="8" height="5.5" fill="#fff"/><path d="M4 5.5l4 3 4-3" stroke="var(--brand-red)" fill="none" stroke-width="0.9"/></svg>t.salwi@gokbrtrips.com</li>
      <li><svg viewBox="0 0 16 16" aria-hidden="true"><circle cx="8" cy="8" r="7" fill="var(--brand-red)"/><circle cx="8" cy="8" r="3.6" fill="none" stroke="#fff" stroke-width="1"/><path d="M4.4 8h7.2M8 4.4v7.2" stroke="#fff" stroke-width="0.8"/></svg>www.gokbrtrips.com</li>
    </ul>
  </article>
</main>
</body>
</html>
```